VORLEN Website Design

We need a website designed for our company VORLEN. We are a luxury lifestyle club that will provide benefits and services for our members. The site should be clean & sleek, preferably using black and white (or darker colors). (example sites: brimvale.example, tusko.example)

Here is a link of a sample page I did using wix. (https://pelmundry4.sitebuild.example/mypage) This can be used to get a general idea.

Target Market(s)

Upper Middle Class in the United States

Number of Pages Required

5+ page

Font styles to use
Sans Serif
Other font styles liked:
• Arial (or other similar fonts)

Requirements
Must have
• A clean design that is eye-catching and speaks to our company.
Nice to have
• Ideas for copy.

```html
<!DOCTYPE html>
<html lang="en">
<head>
<meta charset="UTF-8">
<title>VORLEN — About</title>
<link rel="stylesheet" href="https://fonts.googleapis.com/css2?family=Montserrat:wght@300;400;500;600;700&display=swap">
<style>
  :root {
    --bg: #070b17;
    --panel-a: #0c1433;
    --panel-b: #0a1a2b;
    --text: #ffffff;
    --text-soft: #e6e8ee;
  }
  * { margin: 0; padding: 0; box-sizing: border-box; }
  html, body { width: 1200px; height: 977px; overflow: hidden; background: var(--bg); }
  body { font-family: "Montserrat", Arial, sans-serif; color: var(--text); position: relative; }
  .backdrop { position: absolute; inset: 0; }
  .site-header { position: absolute; left: 0; top: 0; width: 1200px; height: 96px; }
  .brand { position: absolute; left: 150px; top: 30px; font-size: 31px; font-weight: 400; letter-spacing: 0.04em; }
  .main-nav { position: absolute; right: 120px; top: 39px; display: flex; gap: 26px; }
  .main-nav a { color: var(--text-soft); text-decoration: none; font-size: 13px; letter-spacing: 0.03em; font-weight: 400; }
  .main-nav a.is-current { font-weight: 700; color: var(--text); }
  .about { position: absolute; left: 136px; top: 208px; width: 840px; }
  .about-title { font-weight: 300; font-size: 50px; line-height: 48px; }
  .about-title strong { display: block; font-weight: 500; letter-spacing: 0.05em; }
  .tagline { margin-top: 42px; font-size: 20px; font-weight: 400; letter-spacing: 0.3em; }
  .about-copy { margin-top: 30px; }
  .about-copy p { font-size: 15px; line-height: 26px; letter-spacing: 0.15em; margin-bottom: 26px; color: var(--text-soft); }
  .apply-button { display: inline-flex; align-items: center; justify-content: center; width: 142px; height: 44px; border: 2px solid var(--text); border-radius: 22px; color: var(--text); text-decoration: none; font-size: 14px; font-weight: 600; margin-top: -2px; }
  .site-footer { position: absolute; left: 0; width: 1200px; top: 910px; text-align: center; }
  .footer-label { font-size: 12px; font-weight: 700; letter-spacing: 0.02em; }
  .social-links { display: flex; justify-content: center; gap: 12px; margin-top: 8px; }
  .social-links span { width: 14px; height: 14px; border-radius: 50%; background: #c9ccd4; display: block; }
</style>
</head>
<body>
  <svg class="backdrop" width="1200" height="977" role="img" aria-label="Faint low-poly navy texture on the right side">
    <defs>
      <linearGradient id="panelTone" x1="0" y1="0" x2="1" y2="1">
        <stop offset="0" stop-color="#0a1a2a"/>
        <stop offset="0.5" stop-color="#0c1433"/>
        <stop offset="1" stop-color="#0b1428"/>
      </linearGradient>
    </defs>
    <polygon points="992,0 1200,0 1200,977 692,977 492,383" fill="url(#panelTone)"/>
  </svg>

  <header class="site-header">
    <div class="brand">VORLEN</div>
    <nav class="main-nav">
      <a href="#">HOME</a>
      <a href="#" class="is-current">ABOUT</a>
      <a href="#">SERVICES AND BENEFITS</a>
      <a href="#">APPLY</a>
      <a href="#">CONTACT</a>
    </nav>
  </header>

  <main class="about">
    <h1 class="about-title">About<strong>VORLEN</strong></h1>
    <h2 class="tagline">The ultimate full service lifestyle club</h2>
    <div class="about-copy">
      <p>VORLEN was formed to bring the best services, experiences, and exclusive opportunities to our members.</p>
      <p>With everything from private member events to pirvate jet travel, the persk of being a VORLEN member are unmatched.</p>
      <p>Professional athletes, artists, musicians, corporate professionals: Our members come from diverse backgrounds.</p>
      <p>Comprehensive services like 24/7 conceirge, accountants, attorneys, private advisers, planners, investment advisors and more.</p>
    </div>
    <a href="#" class="apply-button">Apply</a>
  </main>

  <footer class="site-footer">
    <div class="footer-label">CONTACT US</div>
    <div class="social-links">
      <span aria-label="Video channel"></span>
      <span aria-label="Photo profile"></span>
      <span aria-label="Microblog profile"></span>
      <span aria-label="Social profile"></span>
      <span aria-label="Community profile"></span>
    </div>
  </footer>
</body>
</html>
```